Darin Wekel Orthodontics
Business Card, Letterhead, Envelopes, Folder
@ Project holder : Please,Extend this Contest.
I am interested and Coming....
Anyone do a full size envelope where the letterhead slides in the envelope unfolded.
Anyone willing to experiment by putting the log and info at the bottom of the stationary page rather than the top.
Thanks for your submissions.#2,3,6,7 appear too busy for me. Lets stick with simplicity. Back of business card should probably have a white or light background so we can write the appoitment time in pen on the card.
ai format uploaded
kindly upload ai or eps file of logo

```html
<!DOCTYPE html>
<html lang="en">
<head>
<meta charset="utf-8">
<title>Darin Wekel Orthodontics — Stationery</title>
<link rel="stylesheet" href="https://fonts.googleapis.com/css2?family=Raleway:wght@300;400;500&display=swap">
<style>
:root{
  --stage:#e6e3de;
  --paper:#ffffff;
  --folder-grey:#e9ebed;
  --blue-deep:#0d3656;
  --blue-mid:#1c5a86;
  --blue-glow:#2f78a8;
  --blue-line:#6fbbe4;
  --ink:#3d4a55;
  --ink-soft:#8a96a0;
  --card-back:#eef0f1;
}
*{box-sizing:border-box;margin:0;padding:0}
html,body{width:1200px;height:487px;overflow:hidden}
body{background:var(--stage);font-family:"Raleway",sans-serif;color:var(--ink);position:relative}
.piece{position:absolute;box-shadow:0 2px 6px rgba(0,0,0,.18)}

/* Brand name set as text */
.brand{font-family:"Raleway",sans-serif;font-weight:300;color:#fff;letter-spacing:.5px;line-height:1;text-align:center}
.brand .sub{display:block;font-size:.36em;margin-top:.25em;letter-spacing:2px;color:#fff}

/* Folder */
.folder{left:19px;top:19px;width:497px;height:329px;background:var(--folder-grey);overflow:hidden}
.folder svg{position:absolute;inset:0}
.folder-fold{position:absolute;left:248px;top:0;width:1px;height:100%;background:rgba(255,255,255,.25)}
.folder-web{position:absolute;left:14px;top:8px;font-size:5px;color:var(--ink-soft)}
.folder-address{position:absolute;left:14px;top:272px;font-size:5px;line-height:1.5;color:#fff}
.folder-tagline{position:absolute;left:296px;top:292px;font-size:6px;color:#fff;letter-spacing:.3px}
.folder .brand.main{position:absolute;left:300px;top:168px;font-size:30px}
.folder .brand.faint{position:absolute;left:50px;top:172px;font-size:30px;color:rgba(255,255,255,.12)}
.folder .brand.faint .sub{color:rgba(255,255,255,.12)}
.pockets{left:19px;top:348px;width:497px;height:96px;background:linear-gradient(180deg,var(--blue-mid),var(--blue-deep));overflow:hidden}
.pockets svg{position:absolute;inset:0}

/* Letterhead */
.letterhead{left:533px;top:29px;width:261px;height:348px;background:var(--paper)}
.lh-band{position:absolute;left:0;top:12px;width:100%;height:30px;background:linear-gradient(90deg,var(--blue-deep),var(--blue-glow) 50%,var(--blue-deep));display:flex;align-items:center;justify-content:center}
.lh-band .brand{font-size:14px}
.lh-rule{position:absolute;left:0;top:43px;width:100%;height:2px;background:var(--blue-line)}
.lh-footer{position:absolute;left:0;bottom:10px;width:100%;text-align:center;font-size:4.2px;color:var(--ink-soft)}

/* Business cards */
.card{width:132px;height:80px;border-radius:5px}
.card-front{left:852px;top:29px;background:radial-gradient(ellipse at 60% 55%,var(--blue-glow),var(--blue-deep) 80%);color:#fff}
.card-front .brand{position:absolute;left:42px;top:28px;font-size:17px}
.card-name{position:absolute;left:8px;top:7px;font-size:4.5px;line-height:1.5}
.card-contact{position:absolute;right:8px;top:7px;font-size:4.5px;line-height:1.5;text-align:right}
.card-back{left:936px;top:100px;background:var(--card-back);padding:16px 12px}
.appt-label{font-size:5px;color:var(--ink-soft);margin-bottom:4px}
.appt-line{display:flex;align-items:flex-end;gap:4px;font-size:5px;color:var(--ink-soft);margin-bottom:9px}
.appt-line span{flex:1;border-bottom:.6px solid #b9c1c7;height:6px}

/* Envelope */
.envelope{left:852px;top:216px;width:300px;height:144px;background:var(--paper);overflow:hidden}
.envelope svg{position:absolute;inset:0}
.env-band{position:absolute;left:0;top:44px;width:100%;height:34px;background:linear-gradient(90deg,var(--blue-deep),var(--blue-glow) 50%,var(--blue-deep));display:flex;align-items:center;justify-content:center}
.env-band .brand{font-size:16px}
.env-rule{position:absolute;left:0;top:79px;width:100%;height:2px;background:var(--blue-line)}
.env-footer{position:absolute;left:0;bottom:10px;width:100%;text-align:center;font-size:4.2px;color:var(--ink-soft)}
</style>
</head>
<body>

<section class="piece folder" aria-label="Presentation folder, outside">
  <svg viewBox="0 0 497 329" width="497" height="329" aria-hidden="true">
    <defs>
      <radialGradient id="folderBlue" cx="0.35" cy="0.5" r="0.7">
        <stop offset="0" stop-color="#2f78a8"/>
        <stop offset="0.6" stop-color="#1c5a86"/>
        <stop offset="1" stop-color="#0d3656"/>
      </radialGradient>
    </defs>
    <path d="M0,329 L0,250 C0,110 110,14 300,12 C400,11 470,40 497,110 L497,329 Z" fill="url(#folderBlue)"/>
    <path d="M0,250 C0,110 110,14 300,12 C400,11 470,40 497,110" fill="none" stroke="#6fbbe4" stroke-width="3"/>
    <path d="M0,256 C4,118 114,22 300,20 C396,19 462,46 497,118" fill="none" stroke="#ffffff" stroke-width="1" opacity=".5"/>
  </svg>
  <div class="folder-fold"></div>
  <p class="folder-web">www.darinwekel.com</p>
  <p class="brand faint">Darin Wekel<span class="sub">orthodontics</span></p>
  <p class="brand main">Darin Wekel<span class="sub">orthodontics</span></p>
  <address class="folder-address">1840 Harbor Lane, Suite 210<br>Rivermont, CA 90411<br>(555) 214-7730</address>
  <p class="folder-tagline">the smile we build, your confidence grows</p>
</section>

<section class="piece pockets" aria-label="Folder inside pockets">
  <svg viewBox="0 0 497 96" width="497" height="96" aria-hidden="true">
    <line x1="248" y1="0" x2="248" y2="96" stroke="#ffffff" stroke-opacity=".25"/>
    <path d="M70,40 L90,60 M90,40 L70,60" stroke="#6fbbe4" stroke-opacity=".4" stroke-width="1"/>
    <path d="M160,40 L180,60 M180,40 L160,60" stroke="#6fbbe4" stroke-opacity=".4" stroke-width="1"/>
    <path d="M0,10 Q248,30 497,10" fill="none" stroke="#6fbbe4" stroke-opacity=".35"/>
  </svg>
</section>

<section class="piece letterhead" aria-label="Letterhead">
  <div class="lh-band"><p class="brand">Darin Wekel<span class="sub">orthodontics</span></p></div>
  <div class="lh-rule"></div>
  <p class="lh-footer">1840 Harbor Lane, Suite 210, Rivermont, CA 90411 · Phone (555) 214-7730 · www.darinwekel.com</p>
</section>

<section class="piece card card-front" aria-label="Business card front">
  <p class="card-name">Darin Wekel, DDS<br>Orthodontist</p>
  <p class="card-contact">(555) 214-7730<br>hello@darinwekel.com<br>www.darinwekel.com</p>
  <p class="brand">Darin Wekel<span class="sub">orthodontics</span></p>
</section>

<section class="piece card card-back" aria-label="Business card back, appointment reminder">
  <p class="appt-label">Your next appointment is on</p>
  <p class="appt-line">Date <span></span></p>
  <p class="appt-line">Time <span></span></p>
</section>

<section class="piece envelope" aria-label="Envelope">
  <svg viewBox="0 0 300 144" width="300" height="144" aria-hidden="true">
    <path d="M0,0 L150,40 L300,0" fill="none" stroke="#d6dbdf" stroke-width="1"/>
  </svg>
  <div class="env-band"><p class="brand">Darin Wekel<span class="sub">orthodontics</span></p></div>
  <div class="env-rule"></div>
  <p class="env-footer">1840 Harbor Lane, Suite 210, Rivermont, CA 90411 · Phone (555) 214-7730 · www.darinwekel.com</p>
</section>

</body>
</html>
```